PLVT Stationary(Business cards/letter heads/envelopes/e-mail signatures)
Letterheads and business card designs
PLVT Stationary(Business cards/letter heads/envelopes/e-mail signatures) - Information Technology
Creative Brief
Professional
Corin Vashley
CEO
Physical: Merrow House Tinsel Crescent Corporate Park Midrand South Africa Postal: P.O. Box 7391 Fernvale 2047
cvashley@ledgerbase.example
http://ledgerbase.example
Please make a generic version using the details above, we would like to be able to edit business card information for different team members.
Please make sure designs are provided for letter heads, envelopes & e-mail signatures along with the business cards

```html
<!DOCTYPE html>
<html lang="en">
<head>
<meta charset="utf-8">
<title>PLVT Business Card</title>
<link href="https://fonts.googleapis.com/css2?family=Montserrat:wght@800&family=Open+Sans:wght@400;700&display=swap" rel="stylesheet">
<style>
  :root{
    --bg:#e9e9ea;
    --red:#a8101c;
    --red-dark:#7e0a14;
    --ink:#1b1b1b;
    --grey:#6d6d6d;
    --rule:#c9c9c9;
    --paper:#ffffff;
  }
  *{margin:0;padding:0;box-sizing:border-box}
  html,body{width:1200px;height:864px;overflow:hidden;background:var(--bg)}
  .canvas{position:relative;width:1200px;height:864px}
  .card{position:absolute;top:277px;width:530px;height:310px;border-radius:22px;overflow:hidden;box-shadow:0 6px 18px rgba(0,0,0,.18)}
  .card--back{left:55px;background:linear-gradient(135deg,var(--red) 0%,var(--red-dark) 100%)}
  .card--front{left:615px;background:var(--paper)}

  .brand{position:absolute;display:flex;align-items:center;gap:10px;font-family:'Montserrat',sans-serif;font-weight:800;letter-spacing:1px;line-height:1}
  .brand__dot{border-radius:50%}
  .card--back .brand{left:50%;top:50%;transform:translate(-50%,-50%);color:#fff;font-size:40px}
  .card--back .brand__dot{width:30px;height:30px;border:3px solid #fff}
  .card--front .brand{left:60px;top:158px;color:var(--ink);font-size:44px}
  .card--front .brand__dot{width:34px;height:34px;background:var(--red)}

  .contact{position:absolute;left:282px;top:34px;padding-left:14px;border-left:1px solid var(--rule);font-family:'Open Sans',sans-serif;color:var(--grey);font-size:10.5px;line-height:1.55}
  .contact__name{color:var(--red);font-weight:700;font-size:13px}
  .contact__role{color:var(--ink);margin-bottom:6px}
  .contact__list{list-style:none}
  .contact__item{display:flex;align-items:center;gap:7px;white-space:nowrap}
  .contact__icon{width:11px;height:11px;flex:none}
  .contact__item--plain{padding-left:18px}

  .swoosh{position:absolute;left:0;bottom:0;width:530px;height:120px}
</style>
</head>
<body>
<main class="canvas">
  <section class="card card--back" aria-label="Business card back">
    <div class="brand"><span class="brand__dot"></span>PLVT</div>
  </section>

  <section class="card card--front" aria-label="Business card front">
    <div class="brand"><span class="brand__dot"></span>PLVT</div>

    <div class="contact">
      <p class="contact__name">Corin Vashley</p>
      <p class="contact__role">CEO</p>
      <ul class="contact__list">
        <li class="contact__item">
          <svg class="contact__icon" viewBox="0 0 12 12"><circle cx="6" cy="6" r="6" fill="#a8101c"/><path d="M6 2.5a2.2 2.2 0 0 0-2.2 2.2C3.8 6.4 6 9.5 6 9.5s2.2-3.1 2.2-4.8A2.2 2.2 0 0 0 6 2.5z" fill="#fff"/></svg>
          P.O. Box 7391
        </li>
        <li class="contact__item contact__item--plain">Fernvale 2047</li>
        <li class="contact__item">
          <svg class="contact__icon" viewBox="0 0 12 12"><circle cx="6" cy="6" r="6" fill="#a8101c"/><path d="M4 3l1.3 1.5-.6.9c.4.9 1 1.5 1.9 1.9l.9-.6L9 8l-.7 1C5.6 9 3 6.4 3 3.7z" fill="#fff"/></svg>
          +27 11 555 0140
        </li>
        <li class="contact__item">
          <svg class="contact__icon" viewBox="0 0 12 12"><circle cx="6" cy="6" r="6" fill="#a8101c"/><rect x="3.2" y="4.5" width="5.6" height="3.6" fill="#fff"/><rect x="4.2" y="2.8" width="3.6" height="1.5" fill="#fff"/></svg>
          +27 11 555 0141
        </li>
        <li class="contact__item">
          <svg class="contact__icon" viewBox="0 0 12 12"><circle cx="6" cy="6" r="6" fill="#a8101c"/><rect x="4.2" y="2.6" width="3.6" height="6.8" rx=".6" fill="#fff"/></svg>
          +27 82 555 0193
        </li>
        <li class="contact__item">
          <svg class="contact__icon" viewBox="0 0 12 12"><circle cx="6" cy="6" r="6" fill="#a8101c"/><rect x="3" y="3.8" width="6" height="4.4" fill="#fff"/><path d="M3 3.8l3 2.4 3-2.4" stroke="#a8101c" stroke-width=".7" fill="none"/></svg>
          cvashley@ledgerbase.example
        </li>
        <li class="contact__item">
          <svg class="contact__icon" viewBox="0 0 12 12"><circle cx="6" cy="6" r="6" fill="#a8101c"/><circle cx="6" cy="6" r="3" stroke="#fff" stroke-width=".9" fill="none"/><path d="M3 6h6M6 3v6" stroke="#fff" stroke-width=".7"/></svg>
          www.ledgerbase.example
        </li>
      </ul>
    </div>

    <svg class="swoosh" viewBox="0 0 530 120" preserveAspectRatio="none" aria-hidden="true">
      <path d="M0 70 C150 120 330 110 530 20 L530 120 L0 120 Z" fill="#a8101c"/>
      <path d="M0 60 C150 108 330 98 530 8 L530 22 C330 112 150 120 0 74 Z" fill="#1b1b1b"/>
      <path d="M0 80 C160 128 340 118 530 34 L530 120 L0 120 Z" fill="#a8101c"/>
      <path d="M0 76 C160 122 340 112 530 30 L530 36 C340 118 160 128 0 82 Z" fill="#ffffff"/>
    </svg>
  </section>
</main>
</body>
</html>
```